contemporary upscale hair salon

we need a business card design for a modern upscale salon. I would like the card to be vertical, simple, and easy to read. I would like a black matte finish on the info side with white on the back of the card, white lettering with a splash of red incorporated somewhere in there. I also want to incorporate embossing and/or cut out in the letters. The info I would like; Name of the business (Velora Salon) stylist name (Janet) phone number(4075319264) and web address (www.veloraexample.com) I am open to putting shears on the card but without it looking too cheap. Looking for something really modern and edgy. these are just ideas I have, but feel free to show me your creative ideas.
please note: the website is still under construction please do not use any images or colors off the web page. Also i currently do not have a logo, that will be a future project.

```html
<!DOCTYPE html>
<html lang="en">
<head>
<meta charset="utf-8">
<title>Velora Salon – Business Card</title>
<link rel="stylesheet" href="https://fonts.googleapis.com/css2?family=Open+Sans:wght@400;600&family=Questrial&display=swap">
<style>
  :root {
    --backdrop: #e9e9e9;
    --card-black: #050505;
    --card-white: #ffffff;
    --accent-red: #ee3b3b;
    --text-light: #ffffff;
    --text-dark: #111111;
  }
  * { box-sizing: border-box; margin: 0; padding: 0; }
  html, body {
    width: 1200px; height: 1200px; overflow: hidden;
    background: var(--backdrop);
  }
  .sheet { position: relative; width: 1200px; height: 1200px; }
  .card {
    position: absolute; top: 170px;
    width: 500px; height: 860px;
    border-radius: 24px; overflow: hidden;
    box-shadow: 0 10px 30px rgba(0,0,0,0.18);
  }
  /* Info side */
  .card--info { left: 70px; background: var(--card-black); color: var(--text-light); }
  .card__header-art {
    position: absolute; top: 0; left: 0; width: 500px; height: 320px;
    background: linear-gradient(180deg, #d83434 0%, #b02a2a 45%, #5a1515 75%, var(--card-black) 100%);
  }
  .brand {
    position: absolute; left: 0; right: 0; top: 380px;
    display: flex; justify-content: center; align-items: flex-start; gap: 12px;
    font-family: "Open Sans", sans-serif; font-weight: 400;
  }
  .brand__dot {
    width: 16px; height: 16px; border-radius: 50%;
    background: var(--accent-red); margin-top: 18px;
  }
  .brand__name { font-size: 50px; line-height: 1.02; }
  .card--info .brand__name { color: var(--text-light); }
  .rule {
    position: absolute; left: 75px; right: 75px; height: 3px;
    background: var(--accent-red);
  }
  .rule--top { top: 525px; }
  .rule--bottom { top: 640px; }
  .stylist {
    position: absolute; left: 0; right: 0; top: 543px; text-align: center;
    font-family: "Questrial", sans-serif;
  }
  .stylist__name { font-size: 34px; font-weight: 700; letter-spacing: 2px; text-transform: uppercase; }
  .stylist__role { font-size: 28px; margin-top: 2px; }
  .contact {
    position: absolute; left: 0; right: 0; top: 662px; text-align: center;
    font-family: "Questrial", sans-serif; font-size: 30px; line-height: 1.4;
  }
  .social {
    position: absolute; right: 38px; bottom: 34px;
    font-family: "Questrial", sans-serif; font-size: 26px;
    color: var(--accent-red);
  }
  /* Back side */
  .card--back { left: 630px; background: var(--card-white); color: var(--text-dark); }
  .card__shears {
    position: absolute; top: 90px; left: 70px; width: 330px; height: 260px;
    border-radius: 12px;
    background: radial-gradient(ellipse at center, #4a4a4a 0%, #f4f4f4 75%);
    opacity: 0.8;
  }
  .card--back .brand {
    top: auto; bottom: 80px; left: auto; right: 45px; justify-content: flex-end;
  }
  .card--back .brand__name { font-size: 72px; color: var(--text-dark); }
  .card--back .brand__dot { width: 20px; height: 20px; margin-top: 30px; }
</style>
</head>
<body>
<main class="sheet">
  <section class="card card--info" aria-label="Business card, info side">
    <div class="card__header-art" role="img" aria-label="Decorative red vertical line pattern across the top of the card"></div>
    <div class="brand">
      <span class="brand__dot"></span>
      <span class="brand__name">Velora<br>Salon</span>
    </div>
    <div class="rule rule--top"></div>
    <div class="stylist">
      <div class="stylist__name">Janet</div>
      <div class="stylist__role">Hair Stylist</div>
    </div>
    <div class="rule rule--bottom"></div>
    <div class="contact">
      <div class="contact__phone">407 531 9264</div>
      <div class="contact__web">www.veloraexample.com</div>
    </div>
    <div class="social">@velora</div>
  </section>

  <section class="card card--back" aria-label="Business card, back side">
    <div class="card__shears" role="img" aria-label="Black silhouette of open hair-cutting shears"></div>
    <div class="brand">
      <span class="brand__dot"></span>
      <span class="brand__name">Velora<br>Salon</span>
    </div>
  </section>
</main>
</body>
</html>
```